Design Brief: Brisk Harbor Group Business Card Design
Project Overview

Brisk Harbor Group is a strategic partner to entrepreneurs and leadership teams, supporting business growth through clarity, execution, and trusted expertise. We are looking for a premium, modern business card design that reflects confidence, professionalism, and upward momentum.

Main logo the one with gold bar for the Brisk Harbor Group.

This card will be used by executives and staff across the Brisk Harbor Group business.

Brand Personality
Professional but human
Confident but collaborative
Strategic, credible, and execution-focused
Premium without being flashy

This is not a startup, tech gimmick, or overly creative brand.

Card Format
Portrait orientation (vertical)
Standard size: 55 × 90 mm
Two-sided
One corner cut (top-right corner preferred) to subtly represent upward movement and growth

Design must still work if corner cutting is not available with certain printers

Front Side (Contact Details)
Include:
Brisk Harbor Group logo (provided)
Name
Title
Phone number
Email address
Website
Optional: tagline at the bottom

Style:
Clean
Minimal
Plenty of white space
Easy to read

Back Side (Ecosystem / Brand Message)
Include:
Heading such as: “The Brisk Network”
Short 2–3 line description explaining that Brisk is a strategic partner with an ecosystem of specialist professional services businesses operating across Strategic Advisory, Capital Raising, People, & Finance.

This side should reinforce scale, capability, and partnership, not sales messaging.

Colours
Primary brand colours:
Brisk Blue: #0063B0
Deep Blue: #1A3D6D
Gold accent (very subtle use only): #C9A24D

Rules:
No gradients
No bright or neon colours
No heavy textures
Gold should be minimal and refined

Typography
Clean, modern sans-serif
Professional and readable
No script or decorative fonts

What to Avoid
Landscape layouts (Unless recommended based on logo design, which is horizontal in nature)
Overdesigned or cluttered cards
Loud colours or gradients
Trendy effects that won’t age well

Multiple accent colours

Deliverables
Print-ready files (PDF)
Editable source files (AI / PSD)
Front and back designs

Mockups showing the portrait card and cut corner

Target Outcome
A business card that feels:
Executive
Distinctive
Timeless
Aligned to a strategic, multi-division business

Target Market(s)

Business Owners and Executives (Across industries)

Industry/Entity Type

Professional Services

Contact Information for Business Card

First name and Surname, Email address, Cell phone number, website

Font styles to use
Other font styles liked:
• IBM Plex Sans and or Sans Pro

Colors
0054AA
0677BA
7BADD7
CADEEF
E8F1F8

Requirements
Must have
• Include QR code to digital business card.

```html
<!DOCTYPE html>
<html lang="en">
<head>
<meta charset="utf-8">
<title>Brisk Harbor Group – Business Card</title>
<link rel="stylesheet" href="https://fonts.googleapis.com/css2?family=Montserrat:wght@800&family=Roboto:wght@400;700&family=Poppins:wght@400;700&family=Open+Sans:ital,wght@1,600&display=swap">
<style>
  :root {
    --backdrop: #5a5a5a;
    --paper: #ffffff;
    --ink: #111111;
    --night: #000000;
    --brisk-blue: #0a5eb0;
    --gold: #bf9f27;
    --grey-text: #555555;
    --dark-text: #2a2a2a;
    --rule: #555555;
  }
  html, body {
    margin: 0;
    padding: 0;
    width: 1200px;
    height: 1200px;
    overflow: hidden;
    background: var(--backdrop);
  }
  .canvas {
    position: relative;
    width: 1200px;
    height: 1200px;
  }

  /* Front side */
  .card-front {
    position: absolute;
    left: 266px;
    top: 158px;
    width: 688px;
    height: 393px;
    background: var(--paper);
    border-bottom: 12px solid var(--night);
    box-sizing: border-box;
  }
  .brand {
    position: absolute;
    left: 80px;
    top: 136px;
    width: 270px;
  }
  .brand-row {
    display: flex;
    align-items: center;
    gap: 10px;
  }
  .brand-square {
    width: 22px;
    height: 22px;
    background: var(--gold);
    flex: none;
  }
  .brand-name {
    font-family: "Montserrat", sans-serif;
    font-weight: 800;
    font-size: 23px;
    line-height: 1.08;
    color: var(--ink);
    letter-spacing: 0.3px;
    margin: 0;
  }
  .brand-tagline {
    margin: 9px 0 0 32px;
    font-family: "Open Sans", sans-serif;
    font-style: italic;
    font-weight: 600;
    font-size: 9px;
    line-height: 1.3;
    color: var(--dark-text);
  }
  .divider {
    position: absolute;
    left: 359px;
    top: 116px;
    width: 1.5px;
    height: 146px;
    background: var(--rule);
  }
  .person {
    position: absolute;
    left: 386px;
    top: 118px;
  }
  .person-name {
    margin: 0;
    font-family: "Roboto", sans-serif;
    font-weight: 700;
    font-size: 27px;
    line-height: 1;
    color: var(--brisk-blue);
  }
  .person-title {
    margin: 5px 0 0;
    font-family: "Roboto", sans-serif;
    font-weight: 400;
    font-size: 15px;
    color: var(--dark-text);
  }
  .contact-list {
    position: absolute;
    left: 386px;
    top: 196px;
    margin: 0;
    padding: 0;
    list-style: none;
    font-family: "Roboto", sans-serif;
    font-size: 16px;
    color: var(--grey-text);
  }
  .contact-item {
    display: flex;
    align-items: center;
    height: 20.5px;
  }
  .contact-icon {
    width: 14px;
    height: 14px;
    margin-right: 12px;
    flex: none;
  }

  /* Back side */
  .card-back {
    position: absolute;
    left: 260px;
    top: 651px;
    width: 692px;
    height: 395px;
    background: var(--night);
  }
  .back-brand {
    position: absolute;
    left: 0;
    right: 0;
    top: 118px;
    display: flex;
    justify-content: center;
    align-items: center;
    gap: 14px;
  }
  .back-brand-square {
    width: 34px;
    height: 34px;
    background: var(--gold);
  }
  .back-brand-name {
    margin: 0;
    font-family: "Montserrat", sans-serif;
    font-weight: 800;
    font-size: 34px;
    color: var(--paper);
    letter-spacing: 0.5px;
  }
  .network {
    position: absolute;
    left: 0;
    right: 0;
    top: 284px;
    text-align: center;
    font-family: "Poppins", sans-serif;
  }
  .network-title {
    margin: 0;
    font-weight: 700;
    font-size: 20px;
    line-height: 1.1;
    color: var(--gold);
  }
  .network-text {
    margin: 1px 0 0;
    font-weight: 400;
    font-size: 16px;
    line-height: 19.5px;
    color: var(--paper);
    white-space: nowrap;
  }
</style>
</head>
<body>
<main class="canvas">

  <section class="card-front" aria-label="Card front">
    <div class="brand">
      <div class="brand-row">
        <span class="brand-square"></span>
        <p class="brand-name">BRISK HARBOR<br>GROUP</p>
      </div>
      <p class="brand-tagline">Clear Strategy. Steady Momentum.<br>Trusted Results.</p>
    </div>

    <div class="divider"></div>

    <div class="person">
      <h1 class="person-name">DANIEL REEVES</h1>
      <p class="person-title">President</p>
    </div>

    <ul class="contact-list">
      <li class="contact-item">
        <svg class="contact-icon" viewBox="0 0 24 24" aria-hidden="true"><path fill="#bf9f27" d="M6.6 10.8a15.1 15.1 0 0 0 6.6 6.6l2.2-2.2a1 1 0 0 1 1-.25 11.4 11.4 0 0 0 3.6.57 1 1 0 0 1 1 1V20a1 1 0 0 1-1 1A17 17 0 0 1 3 4a1 1 0 0 1 1-1h3.5a1 1 0 0 1 1 1c0 1.25.2 2.45.57 3.57a1 1 0 0 1-.25 1z"/></svg>
        555-014-2087
      </li>
      <li class="contact-item">
        <svg class="contact-icon" viewBox="0 0 24 24" aria-hidden="true"><rect x="2" y="5" width="20" height="14" fill="#bf9f27"/><path d="M2 5l10 8 10-8M2 19l7-7M22 19l-7-7" stroke="#fff" stroke-width="1.6" fill="none"/></svg>
        info@briskharborgroup.com
      </li>
      <li class="contact-item">
        <svg class="contact-icon" viewBox="0 0 24 24" aria-hidden="true"><circle cx="12" cy="12" r="10" fill="#bf9f27"/><path d="M12 2a10 10 0 0 1 0 20M2 12h20M12 2c-3 3-3 17 0 20" stroke="#fff" stroke-width="1.4" fill="none"/></svg>
        www.briskharborgroup.com
      </li>
    </ul>
  </section>

  <section class="card-back" aria-label="Card back">
    <div class="back-brand">
      <span class="back-brand-square"></span>
      <p class="back-brand-name">BRISK HARBOR GROUP</p>
    </div>
    <div class="network">
      <h2 class="network-title">THE BRISK NETWORK</h2>
      <p class="network-text">Brisk brings together a network of specialist<br>professional firms, working side by side in Strategic Advisory,<br>Capital Raising, People, and Finance.</p>
    </div>
  </section>

</main>
</body>
</html>
```